Exciting new female owned mobile Aesthetics company preparing for our first tradeshows!

We are a simple, elegant and fresh female owned concierge/mobile aesthetics company, catering to both men and women ages 30-60. We are looking for booth decoration ideas. We are a service based company that is not selling products, so we need ideas for banners and tabletop designs. We would like the design to match our logo and website colors. Website is at www(dot)fernquill(dot)com.

Target Market(s)

30-60 year old men and women, but mostly women

Industry/Entity Type

beauty and aesthetics

Font styles to use
Sans Serif
Script

Requirements
Must have
• Retractable Banner designs (33inch x 80inch) All designs need to match colors and design of logo and website at fernquill(dot)com

```html
<!DOCTYPE html>
<html lang="en">
<head>
<meta charset="utf-8">
<title>Fernquill Retractable Banner</title>
<link rel="stylesheet" href="https://fonts.googleapis.com/css2?family=Cookie&family=Cinzel:wght@400&display=swap">
<style>
  :root {
    --stage: #c9c9c9;
    --charcoal: #2e2d33;
    --paper: #f7f3f7;
    --pink: #f42c9a;
    --pink-deep: #ec2f8c;
    --orange: #fb8a2c;
    --ink: #26242a;
    --hair: #8c2b22;
    --skin: #f2c9b8;
  }
  * { margin: 0; padding: 0; box-sizing: border-box; }
  html, body { width: 1200px; height: 3474px; overflow: hidden; background: var(--stage); }
  .banner {
    position: absolute; left: 50px; top: 404px;
    width: 1100px; height: 2666px;
    background: var(--paper);
    overflow: hidden;
    box-shadow: 0 6px 18px rgba(0,0,0,.35);
    font-family: 'Cookie', cursive;
  }
  .banner__shapes { position: absolute; inset: 0; width: 1100px; height: 2666px; }
  .portrait {
    position: absolute; left: 524px; top: 0; width: 576px; height: 960px;
    background: linear-gradient(180deg, var(--hair) 0%, #b5573f 30%, var(--skin) 55%, #e9b4a2 100%);
    border-top-left-radius: 260px 420px;
  }
  .brand {
    position: absolute; left: 60px; top: 2390px; width: 0; height: 0;
  }
  .brand-lockup {
    position: absolute; left: 60px; top: 540px; width: 480px; text-align: center;
  }
  .brand-lockup__mark {
    width: 46px; height: 46px; border-radius: 50%;
    background: var(--orange); margin: 0 auto 14px;
  }
  .brand-lockup__name {
    font-size: 150px; line-height: 1; color: var(--orange); font-weight: 400;
  }
  .brand-lockup__tagline {
    font-family: 'Cinzel', serif; font-size: 26px; letter-spacing: 9px;
    color: var(--orange); margin-top: 20px;
  }
  .headline {
    position: absolute; left: 0; top: 1150px; width: 1100px; text-align: center;
    font-size: 168px; line-height: 168px;
  }
  .headline__pink { color: var(--pink); }
  .headline__orange { color: var(--orange); }
  .services-tab {
    position: absolute; left: 337px; top: 1894px; width: 426px; height: 117px;
    background: linear-gradient(90deg, var(--orange), #f96a4a 70%, var(--pink));
    border-radius: 48px 0 48px 0;
    color: #fff; font-size: 78px; line-height: 117px; text-align: center;
  }
  .services {
    position: absolute; left: 65px; top: 2055px; width: 970px;
    display: flex; justify-content: space-between; list-style: none;
  }
  .services__item {
    width: 313px; height: 79px; border: 4px solid var(--pink); border-radius: 16px;
    background: #fff; color: var(--ink); font-size: 54px; line-height: 72px; text-align: center;
  }
  .contact {
    position: absolute; left: 0; top: 2370px; width: 1100px; text-align: center; color: #fff;
  }
  .contact__phone { font-size: 140px; line-height: 150px; }
  .contact__web { font-size: 76px; line-height: 80px; }
</style>
</head>
<body>
  <section class="banner">
    <svg class="banner__shapes" viewBox="0 0 1100 2666" aria-hidden="true">
      <rect x="0" y="0" width="1100" height="1040" fill="var(--charcoal)"/>
      <path d="M0 1040 C 300 1120, 700 960, 1100 1000 L1100 1120 L0 1120 Z" fill="var(--paper)"/>
      <path d="M0 1030 C 250 1120, 600 990, 1100 960 L1100 985 C 620 1010, 300 1140, 0 1080 Z" fill="var(--pink)"/>
      <path d="M380 1050 C 650 970, 900 950, 1100 960 L1100 990 C 900 975, 700 990, 380 1050 Z" fill="var(--orange)"/>
      <path d="M0 2280 C 300 2360, 700 2200, 1100 2300 L1100 2666 L0 2666 Z" fill="var(--pink)"/>
      <path d="M0 2255 C 320 2320, 700 2160, 1100 2240 L1100 2275 C 700 2190, 320 2350, 0 2285 Z" fill="var(--ink)"/>
    </svg>

    <div class="portrait" role="img" aria-label="Illustrated portrait of a red-haired woman with pink lips"></div>

    <div class="brand-lockup">
      <div class="brand-lockup__mark"></div>
      <div class="brand-lockup__name">Fernquill</div>
      <div class="brand-lockup__tagline">CONCIERGE AESTHETICS</div>
    </div>

    <h1 class="headline">
      <span class="headline__pink">Live Life On</span><br>
      <span class="headline__pink">Your Own Time</span><br>
      <span class="headline__orange">Fernquill</span><br>
      <span class="headline__orange">Comes To You!</span>
    </h1>

    <div class="services-tab">Our Services</div>
    <ul class="services">
      <li class="services__item">Private Session</li>
      <li class="services__item">Group Session</li>
      <li class="services__item">Fernquill Party</li>
    </ul>

    <div class="contact">
      <div class="contact__phone">(208) 555-0147</div>
      <div class="contact__web">www.fernquill.com</div>
    </div>
  </section>
</body>
</html>
```